Corvell Staffing Partners Business Cards

Business cards with logo design for a new recruiting company called "Corvell Staffing Partners"

incorporate RED & BLUE colors

Final design should reflect strength - clean, elegant design

Company name superimposed upon graphic (Greek Columns)

Please see attached Photos!!!

Industry/Entity Type

Business

Font styles to use
Decorative

Colors
ec2027
0555a3
85cae6

Requirements
Must have
• Must look very similar to attached design!!!

Want Company name superimposed upon graphic (Greek Columns)

Tag line at bottom must be included:
"Empowering Exceptional Companies with Exceptional People"

```html
<!DOCTYPE html>
<html lang="en">
<head>
<meta charset="utf-8">
<title>Corvell Staffing Partners – Business Card</title>
<link rel="stylesheet" href="https://fonts.googleapis.com/css2?family=Lato:wght@400;700;900&display=swap">
<style>
  :root {
    --brand-red: #ec2027;
    --brand-blue: #0555a3;
    --brand-sky: #85cae6;
    --ink: #1d1d1f;
    --paper: #ffffff;
    --backdrop: #e4e6e9;
  }
  * { margin: 0; padding: 0; box-sizing: border-box; }
  html, body {
    width: 1200px;
    height: 900px;
    overflow: hidden;
    background: var(--backdrop);
    font-family: "Lato", sans-serif;
  }
  .stage {
    position: relative;
    width: 1200px;
    height: 900px;
  }
  .business-card {
    position: absolute;
    left: 100px;
    top: 164px;
    width: 1000px;
    height: 572px;
    background: var(--paper);
    overflow: hidden;
    box-shadow: 0 10px 30px rgba(0, 0, 0, 0.18);
  }
  .brand-lockup {
    position: absolute;
    left: 70px;
    top: 60px;
    width: 360px;
    display: flex;
    flex-direction: column;
    align-items: center;
    gap: 20px;
  }
  .brand-square {
    width: 34px;
    height: 34px;
    background: var(--brand-red);
  }
  .brand-name {
    font-weight: 900;
    font-size: 52px;
    line-height: 1.1;
    text-align: center;
    color: var(--brand-blue);
  }
  .person {
    position: absolute;
    right: 88px;
    top: 62px;
    display: inline-flex;
    flex-direction: column;
    align-items: flex-end;
  }
  .person-name {
    font-size: 42px;
    font-weight: 400;
    color: var(--brand-blue);
    letter-spacing: 0.2px;
  }
  .person-name strong { font-weight: 700; }
  .person-title {
    margin-top: 4px;
    font-size: 17px;
    font-weight: 700;
    letter-spacing: 2px;
    color: var(--brand-red);
  }
  .contact-list {
    position: absolute;
    left: 560px;
    top: 214px;
    list-style: none;
  }
  .contact-item {
    display: flex;
    align-items: center;
    gap: 14px;
    font-size: 26px;
    color: var(--ink);
    height: 42px;
  }
  .contact-icon {
    width: 22px;
    height: 22px;
    flex: none;
    fill: var(--brand-red);
  }
  .swoosh {
    position: absolute;
    left: 0;
    top: 0;
    width: 1000px;
    height: 572px;
  }
  .swoosh .band { fill: var(--brand-blue); }
  .swoosh .accent { fill: var(--brand-red); }
  .tagline {
    position: absolute;
    left: 0;
    right: 0;
    bottom: 36px;
    text-align: center;
    font-size: 31px;
    font-weight: 400;
    color: var(--paper);
    letter-spacing: 0.3px;
  }
  .tagline strong { font-weight: 700; }
</style>
</head>
<body>
<main class="stage">
  <section class="business-card">
    <svg class="swoosh" viewBox="0 0 1000 572" aria-hidden="true">
      <path class="accent" d="M0 462 Q 560 362 1000 394 L1000 408 Q 560 378 0 476 Z"/>
      <path class="band" d="M0 474 Q 560 376 1000 406 L1000 572 L0 572 Z"/>
    </svg>

    <div class="brand-lockup">
      <span class="brand-square"></span>
      <p class="brand-name">Corvell<br>Staffing<br>Partners</p>
    </div>

    <div class="person">
      <h1 class="person-name">Daniel <strong>R</strong> Whitcombe</h1>
      <p class="person-title">PRESIDENT</p>
    </div>

    <ul class="contact-list">
      <li class="contact-item">
        <svg class="contact-icon" viewBox="0 0 24 24" aria-hidden="true"><path d="M3 8c0-3 4-5 9-5s9 2 9 5v2h-5V8c-1-.6-2.4-1-4-1s-3 .4-4 1v2H3zM6 12h12l2 8H4z"/></svg>
        <span>512 555 0148</span>
      </li>
      <li class="contact-item">
        <svg class="contact-icon" viewBox="0 0 24 24" aria-hidden="true"><path d="M2 3h20v14H13v2h4v2H7v-2h4v-2H2zm2 2v10h16V5z"/></svg>
        <span>CorvellSP.com</span>
      </li>
      <li class="contact-item">
        <svg class="contact-icon" viewBox="0 0 24 24" aria-hidden="true"><path d="M2 4h20v16H2zm2.5 2 7.5 6 7.5-6zM4 8v10h16V8l-8 6.4z"/></svg>
        <span>DWhitcombe@CorvellSP.com</span>
      </li>
    </ul>

    <p class="tagline">Empowering <strong>Exceptional</strong> Companies with <strong>Exceptional</strong> People</p>
  </section>
</main>
</body>
</html>
```